National Australian HR & Recruitment Company

we need a document design (letter head / footer) for a proposal document to send to clients. This needs to include a design for the front page and some kind of water mark or design throughout the document.
The document needs to remain workable (word.doc) not PDF
The design should be elegant and corporate looking
The document is attached

Target Market(s)

Human Resource Managers. Corporate Clients

Industry/Entity Type

It Company

Font styles to use
Sans Serif

Requirements
Must have
• Must have a sleek elegant look

```html
<!DOCTYPE html>
<html lang="en">
<head>
<meta charset="utf-8">
<title>An Overview – Next Step</title>
<link rel="stylesheet" href="https://fonts.googleapis.com/css2?family=Arimo:wght@400;700&display=swap">
<style>
  :root {
    --green: #2e9e4a;
    --green-dark: #1f7a36;
    --green-light: #8fcf8f;
    --ink: #222;
    --paper: #fff;
  }
  * { box-sizing: border-box; margin: 0; padding: 0; }
  html, body { width: 849px; height: 1200px; overflow: hidden; background: var(--paper); }
  .page {
    position: relative; width: 849px; height: 1200px; overflow: hidden;
    font-family: "Arimo", Arial, sans-serif; color: var(--ink);
  }
  .corner { position: absolute; top: 0; right: 0; }
  .title {
    position: absolute; left: 74px; top: 30px;
    font-size: 25px; font-weight: 700; color: var(--green);
  }
  .title-rule {
    position: absolute; left: 74px; right: 74px; top: 66px;
    height: 3px; background: var(--green);
  }
  .letter {
    position: absolute; left: 74px; right: 74px; top: 100px;
    font-size: 14.6px; line-height: 22px; text-align: justify;
  }
  .letter p { margin-bottom: 21px; }
  .signature {
    width: 110px; height: 54px; margin: -8px 0 10px;
    background: linear-gradient(90deg, #e8ecf3, #f4f6fa); border-radius: 4px;
  }
  .signer { font-weight: 700; margin-bottom: 0; }
  .footer-band {
    position: absolute; left: 0; right: 0; top: 1108px; height: 38px;
    background: linear-gradient(90deg, var(--paper) 0%, #e7f4e6 40%, var(--green-light) 100%);
    display: flex; align-items: center; justify-content: flex-end;
    gap: 42px; padding-right: 60px; font-size: 12.5px; color: var(--green-dark);
  }
  .base { position: absolute; left: 0; bottom: 0; }
</style>
</head>
<body>
<div class="page">
  <svg class="corner" width="140" height="70" viewBox="0 0 140 70" aria-hidden="true">
    <polygon points="40,0 140,0 140,70" fill="var(--green-dark)"/>
  </svg>

  <h1 class="title">An Overview</h1>
  <div class="title-rule"></div>

  <div class="letter">
    <p>Dear Marlene,</p>
    <p>Thank you for reaching out to Next Step to offer us the opportunity to assist your employee through our outplacement and career transition services.</p>
    <p>We understand that as a responsible employer, providing outplacement is about much more than mitigating employment legislation or safeguarding your employer brand. The reality is that most of our clients simply want to help their employees by reducing stress and finding new opportunities quickly.</p>
    <p>However, when looking to provide outplacement support for your staff, it is hard to negotiate the balance between cost and quality. How do you provide flexible, tailored support that is meaningful and effective for each employee without breaking the budget?</p>
    <p>We work with you to create high impact, tailored and cost effective outplacement support for your employees, with programmes to suit all levels and functions within the organisation. We focus on helping you to provide more of what matters for your employees; personalised, practical career transition support which gives them confidence to define and shape their own path.</p>
    <p>Our essentials cover Jobs Search Strategy, Resume Tips, Advice on applying for jobs, The Hidden Job Market, Networking &amp; Social Media, Understanding Advertisements, Using Recruitment Agencies, Basic Interview Preparation and Coping with Change.</p>
    <p>We have provided program options to suit Corvane Industries unique needs, the details of which are outlined in the following pages.</p>
    <p>We pride ourselves on our ability to be flexible and will tailor our programs to you, so please ask if there is anything else we can do, or if at any stage you'd like some advice on the redundancy or outplacement process.</p>
    <p>We look forward to being of assistance.</p>
    <p>Warm regards,</p>
    <div class="signature" role="img" aria-label="Handwritten signature"></div>
    <p class="signer">Priya Hollis MAHRI<br>General Manager</p>
  </div>

  <div class="footer-band">
    <span>1300 555 018</span>
    <span>www.nextstepcareers.com.au</span>
    <span>Page 2</span>
  </div>

  <svg class="base" width="849" height="54" viewBox="0 0 849 54" aria-hidden="true">
    <path d="M0,54 L0,30 C250,6 560,4 849,20 L849,54 Z" fill="var(--green)"/>
    <path d="M0,54 L0,42 C300,22 580,24 849,34 L849,54 Z" fill="var(--green-dark)"/>
  </svg>
</div>
</body>
</html>
```